Corporate Design Glasanlagen
Zielgruppe
Individuelle Fertigung von Glasanlagen (Duschabtrennungen, Glasrückwände, Glastüren, Glastrennwände, Spiegel, Lichtspiegel, Spiegelschränke, Ablagen, Waschtische, Digitaldruck)
Individuelle Anfertigung von Möbeln (Badmöbel, Sideboards, Schränke, Regale, Plattenlösungen)
Aufgabenstellung
Ein passender Slogan kann muss aber nicht hinzugefügt werden,
Klares Design, 1 - 2 Farben, Grautöne sind zusätzlich möglich,
Keine Rottöne,
zusätzliche Infos:
Holzoptik möglich (im Logo oder als Hintergrund)
im Würmtal liegt der naturbelassener Bach, die Würm
Logo oberhalb des Schriftzuges

```html
<!DOCTYPE html>
<html lang="de">
<head>
<meta charset="utf-8">
<title>Isental Werkstätte – Geschäftsausstattung</title>
<link rel="stylesheet" href="https://fonts.googleapis.com/css2?family=Nunito:wght@400;800&family=Arimo:wght@400&display=swap">
<style>
  :root {
    --slate: #676b72;
    --paper: #ffffff;
    --card-light: #f2f3f5;
    --window: #e8eef5;
    --text-soft: #8a8e94;
    --canvas: #ffffff;
    --paper-shadow: 0 3px 9px rgba(0, 0, 0, 0.22), 0 0 2px rgba(0, 0, 0, 0.08);
  }
  * { margin: 0; padding: 0; box-sizing: border-box; }
  html, body { width: 1200px; height: 706px; overflow: hidden; background: var(--canvas); }
  body { position: relative; font-family: "Arimo", Arial, sans-serif; color: var(--slate); }
  .piece { position: absolute; background: var(--paper); overflow: hidden; box-shadow: var(--paper-shadow); }
  .wordmark { position: absolute; display: flex; align-items: center; gap: 7px; font-family: "Nunito", Arial, sans-serif; font-weight: 800; color: var(--slate); white-space: nowrap; letter-spacing: 0.2px; }
  .wordmark .mark { width: 1.6em; height: 1.6em; background: currentColor; flex: none; }
  .contact { font-family: "Nunito", Arial, sans-serif; font-size: 5.2px; color: var(--slate); line-height: 1.35; }
  .icon { fill: var(--slate); }
  .web-band { position: absolute; background: var(--slate); clip-path: polygon(4% 0, 100% 0, 100% 100%, 0 100%); display: flex; align-items: center; justify-content: center; gap: 4px; color: #fff; font-family: "Arimo", Arial, sans-serif; font-size: 5px; }
  .web-band svg { width: 6px; height: 6px; fill: #fff; }

  /* envelope back */
  .envelope-back { left: 96px; top: 49px; width: 459px; height: 203px; }
  .envelope-back .flap { position: absolute; left: 0; top: 0; }
  .envelope-back .wordmark { left: 0; width: 459px; top: 36px; justify-content: center; color: #fff; font-size: 13px; }

  /* envelope front */
  .envelope-front { left: 96px; top: 291px; width: 459px; height: 203px; }
  .envelope-front .wordmark { left: 30px; top: 30px; font-size: 14px; }
  .envelope-front .address-window { position: absolute; left: 320px; top: 101px; width: 108px; height: 59px; background: var(--window); border-radius: 6px; }
  .envelope-front .pin { position: absolute; left: 51px; top: 153px; width: 10px; height: 12px; }
  .envelope-front .contact { position: absolute; left: 33px; top: 174px; }
  .envelope-front .web-band { left: 282px; top: 183px; width: 177px; height: 14px; }

  /* business cards */
  .card-front { left: 96px; top: 527px; width: 216px; height: 132px; background: var(--card-light); }
  .card-front .wordmark { left: 21px; top: 25px; font-size: 11px; }
  .card-front .contact-list { position: absolute; left: 130px; top: 62px; list-style: none; }
  .card-front .contact-list li { display: flex; align-items: center; gap: 9px; height: 13px; }
  .card-front .contact-list svg { width: 8px; height: 8px; flex: none; }
  .card-front .web-band { left: 60px; top: 113px; width: 156px; height: 12px; }

  .card-back { left: 340px; top: 528px; width: 216px; height: 132px; background: var(--slate); }
  .card-back .wordmark { left: 14px; top: 43px; font-size: 11px; color: #fff; }
  .card-back .web-band { left: 60px; top: 75px; width: 156px; height: 12px; background: #fff; color: var(--slate); }
  .card-back .web-band svg { fill: var(--slate); }

  /* letterhead */
  .letterhead { left: 743px; top: 68px; width: 406px; height: 574px; }
  .letterhead .web-band { left: 230px; top: 34px; width: 176px; height: 14px; }
  .letterhead .wordmark { left: 72px; top: 57px; font-size: 11.5px; }
  .letterhead .side-strip { position: absolute; left: 0; top: 235px; width: 10px; height: 339px; background: var(--slate); clip-path: polygon(0 0, 100% 1%, 100% 100%, 0 100%); }
  .letterhead .headline { position: absolute; left: 71px; top: 189px; font-size: 17.5px; font-weight: 400; color: #5f636a; }
  .letterhead .body-copy { position: absolute; left: 71px; top: 230px; width: 236px; font-size: 5.9px; line-height: 1.32; color: var(--text-soft); }
  .letterhead .body-copy p { margin-bottom: 7.5px; }
  .letterhead .role { position: absolute; left: 74px; top: 418px; font-size: 11.5px; color: #5f636a; }
  .letterhead .signature { position: absolute; left: 73px; top: 441px; width: 52px; height: 12px; background: linear-gradient(90deg, rgba(103,107,114,0.35), rgba(103,107,114,0.15)); border-radius: 6px; }
  .letterhead .footer { position: absolute; left: 72px; top: 526px; display: flex; }
  .letterhead .footer-item { position: relative; display: flex; flex-direction: column; align-items: flex-start; }
  .letterhead .footer-item svg { width: 11px; height: 11px; margin-bottom: 8px; }
  .letterhead .footer-item .contact { font-size: 5.6px; }
  .letterhead .footer-address { width: 71px; }
  .letterhead .footer-address svg { margin-left: 25px; height: 13px; }
  .letterhead .footer-mail { width: 77px; padding-left: 14px; }
  .letterhead .footer-mail svg { margin-left: 22px; }
  .letterhead .footer-phone { padding-left: 14px; }
  .letterhead .footer-phone svg { margin-left: 18px; }
  .letterhead .divider { position: absolute; top: 522px; width: 1px; height: 52px; background: var(--slate); }
</style>
</head>
<body>

<svg width="0" height="0" style="position:absolute" aria-hidden="true">
  <symbol id="i-globe" viewBox="0 0 16 16">
    <path d="M8 0a8 8 0 1 0 0 16A8 8 0 0 0 8 0Zm5.9 7h-2.6a12 12 0 0 0-1-4.6A6 6 0 0 1 13.9 7ZM8 2.1c.7.9 1.2 2.6 1.3 4.9H6.7C6.8 4.7 7.3 3 8 2.1ZM5.7 2.4a12 12 0 0 0-1 4.6H2.1a6 6 0 0 1 3.6-4.6ZM2.1 9h2.6c.1 1.8.4 3.4 1 4.6A6 6 0 0 1 2.1 9ZM8 13.9c-.7-.9-1.2-2.6-1.3-4.9h2.6c-.1 2.3-.6 4-1.3 4.9Zm2.3-.3c.6-1.200.9-2.8 1-4.6h2.6a6 6 0 0 1-3.6 4.6Z"/>
  </symbol>
  <symbol id="i-pin" viewBox="0 0 12 16">
    <path d="M6 0a6 6 0 0 0-6 6c0 4.5 6 10 6 10s6-5.5 6-10a6 6 0 0 0-6-6Zm0 8.6A2.6 2.6 0 1 1 6 3.4a2.6 2.6 0 0 1 0 5.2Z"/>
  </symbol>
  <symbol id="i-phone" viewBox="0 0 16 16">
    <path d="M3.6.6 6 3c.5.5.5 1.2 0 1.7L4.8 6a9.5 9.5 0 0 0 5.2 5.2L11.3 10c.5-.5 1.2-.5 1.7 0l2.4 2.4c.5.5.5 1.2 0 1.7l-1.3 1.3c-.8.8-2 1-3 .5A17.7 17.7 0 0 1 .1 4.900c-.4-1-.2-2.2.6-3L1.9.6c.5-.5 1.2-.5 1.7 0Z"/>
  </symbol>
  <symbol id="i-mail" viewBox="0 0 16 11">
    <path d="M0 0h16v11H0Zm1.5 1.3v.2L8 6.4l6.5-4.9v-.2Zm0 1.8v6.3l4.3-3.1Zm13 0-4.3 3.2 4.3 3.1ZM7 6.9 1.9 9.7h12.2L9 6.9 8 7.7Z"/>
  </symbol>
</svg>

<!-- envelope back -->
<section class="piece envelope-back" aria-label="Briefumschlag Rückseite">
  <svg class="flap" width="459" height="110" viewBox="0 0 459 110" aria-hidden="true">
    <path fill="var(--slate)" d="M0 0H459Q455 22 437 28L255 97Q229 107 203 97L22 28Q4 22 0 0Z"/>
  </svg>
  <div class="wordmark"><span class="mark"></span>Isental Werkstätte</div>
</section>

<!-- envelope front -->
<section class="piece envelope-front" aria-label="Briefumschlag Vorderseite">
  <div class="wordmark"><span class="mark"></span>Isental Werkstätte</div>
  <div class="address-window"></div>
  <svg class="pin icon"><use href="#i-pin"/></svg>
  <p class="contact">Address Line Example<br>Street, Pl, AB/2</p>
  <div class="web-band"><svg><use href="#i-globe"/></svg>www.isental-werk.de</div>
</section>

<!-- business card front -->
<section class="piece card-front" aria-label="Visitenkarte Vorderseite">
  <div class="wordmark"><span class="mark"></span>Isental Werkstätte</div>
  <ul class="contact-list contact">
    <li><svg class="icon"><use href="#i-pin"/></svg><span>Address Line Example<br>Street, Pl, AB/2</span></li>
    <li><svg class="icon"><use href="#i-phone"/></svg><span>(089) 410 227 58</span></li>
    <li><svg class="icon"><use href="#i-mail"/></svg><span>post@isental-werk.de</span></li>
  </ul>
  <div class="web-band"><svg><use href="#i-globe"/></svg>www.isental-werk.de</div>
</section>

<!-- business card back -->
<section class="piece card-back" aria-label="Visitenkarte Rückseite">
  <div class="wordmark"><span class="mark"></span>Isental Werkstätte</div>
  <div class="web-band"><svg><use href="#i-globe"/></svg>www.isental-werk.de</div>
</section>

<!-- letterhead -->
<section class="piece letterhead" aria-label="Briefbogen">
  <div class="web-band"><svg><use href="#i-globe"/></svg>www.isental-werk.de</div>
  <div class="wordmark"><span class="mark"></span>Isental Werkstätte</div>
  <div class="side-strip"></div>
  <h1 class="headline">Headline here</h1>
  <div class="body-copy">
    <p>Lorem ipsum dolor sit amet, menandri urbanitas prodesset ad pro. Ex pri stet eleifend constituto, causae consetetur qui ex. Qui minimum ullamcorper ex. Illud noluisse est id, ne labore iisque eripuit pro.</p>
    <p>Ei duo vivendum comprehensam. Qui paulo elitr eu, has adipisci tractatos et. Sed causae verear instructior ex, eam oblique mandamus ad. Nusquam iudicabit usu at.</p>
    <p>Ex nam oblique civibus petentium, ex nam eius assentior. Ut argumentum efficiantur has, scripta vulputate et eos. In summo oblique eum, consetetur definitionem eos te. Vel id natum officiis accusata, id vis quot veritus. Vel no deserunt salutandi.</p>
    <p>Has cu tota civibus urbanitas. Duo ei iudico accommodare philosophia. Eu diam brute est. Cum an debet constituam, te brute essent repudiare pri, an nam reque iriure recusabo. Et nam quis saepe persius, mea nobis legendos pertinax ei. Atqui recteque cotidieque pro ad. Ad veri exerci pri.</p>
  </div>
  <p class="role">Manager</p>
  <div class="signature" role="img" aria-label="Handschriftliche Unterschrift"></div>
  <div class="divider" style="left:143px"></div>
  <div class="divider" style="left:220px"></div>
  <div class="footer">
    <div class="footer-item footer-address">
      <svg class="icon"><use href="#i-pin"/></svg>
      <p class="contact">Address Line Example<br>Street, Pl, AB/2</p>
    </div>
    <div class="footer-item footer-mail">
      <svg class="icon"><use href="#i-mail"/></svg>
      <p class="contact">post@isental-werk.de</p>
    </div>
    <div class="footer-item footer-phone">
      <svg class="icon"><use href="#i-phone"/></svg>
      <p class="contact">(089) 410 227 58</p>
    </div>
  </div>
</section>

</body>
</html>
```